Natural Light/Organic/Documentary Photography Business

I like a simple, approachable, feminine, earthy/organic feel. Earth/neutral tones, nothing too loud or obnoxious. I like the watercolor look. I don't want anything too trendy or something I'll get tired of after a couple months. As far as colors, I am much more a fan of cream/taupe/blue/green...not a fan of pink or purple at all.

Target Market(s)

Weddings & Families

Industry/Entity Type

Wedding Photography

Contact Information for Business Card

website, email, phone number

Font styles to use
Other font styles liked:
• Horizontes, Gotham

Colors

Designer to choose colors to be used in the design.

Requirements
Must have
• Website: www.elspethmarlowe.com
• Phone: 412.638.9057
• Email: elspeth@elspethmarlowe.com
Nice to have
• I like the watercolor look but its not necessary. I like simple/earthy tones. Nothing too loud or distracting. Simple & feminine without being too girly. I like an approachable/soft feel.
• Instagram: www.instagram.com/elspethmarlowephotography/
Should not have
• NO loud colors or design or pattern. I do not want a photo of a camera or lens or anything cheesy like that.

```html
<!DOCTYPE html>
<html lang="en">
<head>
<meta charset="utf-8">
<title>Elspeth Marlowe Photography — Business Card</title>
<link rel="stylesheet" href="https://fonts.googleapis.com/css2?family=Montserrat:wght@300;400;500&display=swap">
<style>
  :root {
    --page-bg: #ffffff;
    --card-bg: #ffffff;
    --wash-deep: #c3b3a1;
    --wash-mid: #d6c9ba;
    --wash-light: #ece5dc;
    --panel-bg: #ffffff;
    --panel-rule: #a79b90;
    --ink: #857a71;
    --ink-strong: #6e645c;
  }
  * { margin: 0; padding: 0; box-sizing: border-box; }
  html, body {
    width: 1200px;
    height: 867px;
    overflow: hidden;
    background: var(--page-bg);
    font-family: "Montserrat", Arial, sans-serif;
  }
  .card {
    position: absolute;
    left: 104px;
    top: 128px;
    width: 992px;
    height: 610px;
    background: var(--card-bg);
  }
  .watercolor-wash {
    position: absolute;
    left: 70px;
    top: 62px;
    width: 852px;
    height: 478px;
    background:
      radial-gradient(ellipse 30% 40% at 48% 18%, rgba(255,255,255,0.95), rgba(255,255,255,0) 70%),
      radial-gradient(ellipse 30% 30% at 30% 92%, rgba(255,255,255,0.9), rgba(255,255,255,0) 70%),
      radial-gradient(ellipse 25% 35% at 92% 85%, rgba(255,255,255,0.95), rgba(255,255,255,0) 70%),
      radial-gradient(ellipse 40% 50% at 82% 30%, var(--wash-deep), rgba(195,179,161,0) 80%),
      radial-gradient(ellipse 40% 50% at 12% 45%, var(--wash-deep), rgba(195,179,161,0) 80%),
      linear-gradient(135deg, var(--wash-mid), var(--wash-light) 55%, var(--wash-mid));
  }
  .info-panel {
    position: absolute;
    left: 180px;
    top: 162px;
    width: 632px;
    height: 286px;
    background: var(--panel-bg);
    border: 1px solid var(--panel-rule);
    text-align: center;
    color: var(--ink);
  }
  .brand-name {
    position: absolute;
    left: 0; right: 0;
    top: 52px;
    font-weight: 300;
    font-size: 40px;
    letter-spacing: 1px;
    color: var(--ink-strong);
  }
  .brand-tagline {
    position: absolute;
    left: 0; right: 0;
    top: 113px;
    font-weight: 400;
    font-size: 11px;
    letter-spacing: 6px;
    padding-left: 6px;
    color: var(--ink);
  }
  .contact-list {
    position: absolute;
    left: 0; right: 0;
    top: 180px;
    list-style: none;
    font-size: 12.5px;
    line-height: 24px;
    font-weight: 400;
  }
  .contact-label {
    font-weight: 500;
    color: var(--ink-strong);
  }
  .contact-sep { margin: 0 4px; }
  .contact-gap { margin: 0 12px; }
</style>
</head>
<body>
  <div class="card">
    <div class="watercolor-wash" role="img" aria-label="Soft taupe and cream watercolour wash background"></div>
    <div class="info-panel">
      <h1 class="brand-name">Elspeth Marlowe</h1>
      <p class="brand-tagline">PHOTOGRAPHY</p>
      <ul class="contact-list">
        <li><span class="contact-label">Website</span><span class="contact-sep">|</span>www.elspethmarlowe.com<span class="contact-gap">·</span><span class="contact-label">Phone</span><span class="contact-sep">|</span>412 638 9057</li>
        <li><span class="contact-label">Email</span><span class="contact-sep">|</span>elspeth@elspethmarlowe.com</li>
        <li><span class="contact-label">Instagram</span><span class="contact-sep">|</span>@elspethmarlowephotography</li>
      </ul>
    </div>
  </div>
</body>
</html>
```